どんな物をいくらで貸してくれるのかを知りたいお客様が多く、チラシでアピールしたいと思っています。
まずはメイン商品であるぐるっと稜線セットDX、のびのび高原セット、わいわい焚火セット、ゆるりと星祭セットのセット商品の紹介をしたいです。
その他として個々のレンタル品に関して、こんなものも貸してますという紹介を行いたく、例えば登山テント、寝袋、大型ザック、望遠鏡、釣りセット、BBQセットもそれぞれいくらで貸していますという紹介をサブとして紹介したいです。
最後に店舗紹介という形でお願いいたします。
アウトドアギアレンタルこかげどう/TEL:0544-61-3917,FAX:0544-61-3918/店舗地図/ホームページ、http://www.kokagedou.jp/ぐるっと稜線セットDX 9980~、のびのび高原縦走セット 11980~、わいわい焚火セット 12480円、ゆるりと星祭セット 9800円/ロゴ(添付ファイル)
B4
片面
特にありません
アウトドア雑誌のミルフォさんのようなイメージで製作して頂けたらと思います。

デザインとしてはどれも素晴らしい作品でした。その中で、当選させて頂いた作品は、こちらの言葉足らずな部分を補うように、訴えたかった点を表現して頂いた所を評価させて頂きました。

短時間の中で、沢山の提案本当にありがとうございました。
それぞれ良い部分がありましたので選定で悩みました。
またどうぞ宜しくお願いいたします。

```html
<!DOCTYPE html>
<html lang="ja">
<head>
<meta charset="utf-8">
<title>気軽におしゃれにアウトドア・ガール｜アウトドアギアレンタルこかげどう</title>
<link href="https://fonts.googleapis.com/css2?family=Noto+Sans+JP:wght@400;500;700;900&display=swap" rel="stylesheet">
<style>
:root{
  --pink:#e5407a;
  --red:#d8262f;
  --green:#5a9a2e;
  --blue:#2a8bbf;
  --orange:#e77b22;
  --ink:#333;
  --paper:#fff;
  --cream:#f6f2e8;
  --line:#c9c9c9;
}
*{margin:0;padding:0;box-sizing:border-box}
html,body{width:849px;height:1200px;overflow:hidden;background:var(--paper)}
body{font-family:"Noto Sans JP",sans-serif;color:var(--ink);position:relative}
.flyer{position:absolute;inset:0;width:849px;height:1200px;overflow:hidden}

/* hero */
.hero-photo{position:absolute;left:0;top:0;width:849px;height:600px;
  background:linear-gradient(180deg,#dfe7ee 0%,#eef1ee 35%,#c8c7a4 62%,#9a8f5c 100%)}
.title-line{position:absolute;left:266px;top:24px;width:310px;text-align:center;font-size:37px;font-weight:900;color:var(--pink);letter-spacing:1px;white-space:nowrap;line-height:1.2}
.title-vertical{position:absolute;left:392px;top:84px;writing-mode:vertical-rl;font-size:52px;font-weight:900;color:var(--pink);letter-spacing:2px;line-height:1;white-space:nowrap}

.set-card{position:absolute;background:rgba(255,255,255,.93);padding:12px 14px}
.set-card p{font-size:10.5px;line-height:1.6}
.set-card .price{font-size:26px;font-weight:900;color:var(--red);white-space:nowrap}
.set-card .price small{font-size:15px;font-weight:700;margin-right:6px;color:var(--ink)}

.star-card{left:18px;top:18px;width:232px;height:300px}
.star-card .set-name{position:absolute;left:8px;top:14px;writing-mode:vertical-rl;font-size:17px;font-weight:700;color:var(--green);letter-spacing:2px}
.star-card .photo{position:absolute;left:40px;top:14px;width:178px;height:80px;background:linear-gradient(120deg,#c9272c,#e8574c)}
.star-card .price{position:absolute;left:40px;top:104px}
.star-card .body{position:absolute;left:40px;top:146px;width:180px}

.ridge-card{left:586px;top:14px;width:248px}
.ridge-card .set-name{font-size:15px;font-weight:700;color:var(--green)}
.ridge-card .price{margin:2px 0 6px}
.ridge-card .photos{display:flex;gap:6px;margin-top:10px}
.ridge-card .photo{height:120px;flex:1}
.pack{background:linear-gradient(160deg,#e46a86,#b83a57)}
.jacket{background:linear-gradient(160deg,#f2e447,#c9b91e)}
.boots{height:56px;margin-top:6px;background:linear-gradient(90deg,#7d8f5a,#a0ab72)}

/* middle sets */
.box{position:absolute;top:592px;width:396px;height:170px;border:2px solid var(--blue);background:var(--paper)}
.box.left{left:22px}
.box.right{left:430px}
.box-head{background:var(--blue);color:#fff;display:flex;align-items:baseline;justify-content:space-between;padding:5px 10px}
.box-head h2{font-size:16px;font-weight:700}
.box-head .price{font-size:22px;font-weight:900}
.box-head .price small{font-size:12px;margin-right:4px}
.box-body{display:flex;gap:8px;padding:8px 10px}
.box-body p{font-size:10px;line-height:1.55;flex:1}
.box-body .photo{width:150px;height:118px;flex:none}
.tent{background:linear-gradient(150deg,#7fb7d6,#e8ebe2 60%,#a3a47a)}
.fire{background:linear-gradient(150deg,#b9d6e0,#dfe2d2 55%,#8c8a60)}

/* others */
.others{position:absolute;left:22px;top:774px;width:360px}
.others h2{background:var(--orange);color:#fff;font-size:16px;font-weight:700;padding:4px 10px}
.price-table{width:100%;border-collapse:collapse;font-size:12.5px}
.price-table td{border-bottom:1px dotted var(--line);padding:6px 6px}
.price-table td.yen{text-align:right;font-weight:700;color:var(--red)}
.item-photos{position:absolute;top:774px;left:396px;display:flex;gap:8px}
.item-photos .photo{width:100px;height:150px}
.grill{background:linear-gradient(180deg,#f4f4f4,#c9303a 70%,#777)}
.cooler{background:linear-gradient(180deg,#f4f4f4 40%,#c52b33)}
.scope{background:linear-gradient(180deg,#f4f4f4,#9aa0a8 60%,#3e4248)}
.more-badge{position:absolute;left:730px;top:792px;width:98px;height:98px;border-radius:50%;background:var(--red);color:#fff;display:flex;align-items:center;justify-content:center;text-align:center;font-size:12px;font-weight:700;line-height:1.45}

.note{position:absolute;left:22px;top:948px;width:806px;font-size:10.5px;line-height:1.6;color:var(--red)}

/* store */
.store{position:absolute;left:0;top:996px;width:849px;height:204px;background:var(--cream);border-top:3px solid var(--green)}
.store-label{position:absolute;left:22px;top:14px;background:var(--green);color:#fff;font-size:13px;font-weight:700;padding:3px 12px}
.store-name{position:absolute;left:22px;top:54px;display:flex;align-items:center;gap:10px}
.store-name .mark{width:14px;height:14px;background:var(--green)}
.store-name span{font-size:19px;font-weight:700;color:var(--green);line-height:1.25}
.store-name small{display:block;font-size:11px}
.contact{position:absolute;left:262px;top:14px;width:356px;font-size:12px;line-height:1.7}
.contact .web{font-size:15px;font-weight:700;color:var(--blue)}
.contact .tel{font-size:16px;font-weight:900;color:var(--green);margin-top:4px;white-space:nowrap}
.contact .tag{display:inline-block;background:var(--green);color:#fff;font-size:10px;padding:0 5px;margin-right:6px}
.map{position:absolute;left:628px;top:14px;width:200px;height:150px;background:linear-gradient(135deg,#eef0e6,#d7dcc7)}
.bottom-band{position:absolute;left:0;bottom:0;width:849px;height:22px;background:var(--green)}
</style>
</head>
<body>
<main class="flyer">

  <section class="hero">
    <div class="hero-photo" role="img" aria-label="草原でキャンプを楽しむ女性たちとテントの写真"></div>

    <h1>
      <span class="title-line">気軽におしゃれに</span>
      <span class="title-vertical">アウトドア・ガール</span>
    </h1>

    <article class="set-card star-card">
      <h2 class="set-name">ゆるりと星祭セット</h2>
      <div class="photo" role="img" aria-label="赤い寝袋とテントの写真"></div>
      <div class="price"><small>1泊2日</small>9800円〜</div>
      <div class="body">
        <p>夏の野外イベントに2人で気軽に参加できるセットです。テントと寝袋、マットまで揃っているので手ぶらで出かけられます。</p>
        <p>●セット内容<br>2人用テント／寝袋×2／マット×2／ランタン／チェア×2</p>
      </div>
    </article>

    <article class="set-card ridge-card">
      <h2 class="set-name">ぐるっと稜線セットDX</h2>
      <div class="price"><small>1泊2日</small>9980円〜</div>
      <p>山歩きに必要な装備をひと通り揃えたセットです。人気ブランドのザックやウェアで、初めてでもおしゃれに稜線歩きを楽しめます。</p>
      <p>●セット内容<br>ザック／レインウェア／登山靴／ヘッドランプ</p>
      <div class="photos">
        <div class="photo pack" role="img" aria-label="ピンクの登山ザックの写真"></div>
        <div class="photo jacket" role="img" aria-label="黄色いレインジャケットの写真"></div>
      </div>
      <div class="boots" role="img" aria-label="登山靴の写真"></div>
    </article>
  </section>

  <section class="box left">
    <div class="box-head"><h2>のびのび高原セット</h2><span class="price"><small>1泊2日</small>11980円〜</span></div>
    <div class="box-body">
      <p>のびのび高原縦走セットは山小屋泊にも対応した充実の内容です。ウェアから小物までまとめて借りられるので準備も安心です。<br>●ザック／ウェア／登山靴／ヘッドランプ／ストック</p>
      <div class="photo tent" role="img" aria-label="高原のテントの写真"></div>
    </div>
  </section>

  <section class="box right">
    <div class="box-head"><h2>わいわい焚火セット</h2><span class="price"><small>1泊2日</small>12480円〜</span></div>
    <div class="box-body">
      <p>仲間や家族でわいわい楽しめる大人数向けのセットです。大型テントとタープ、焚火台まで揃っています。<br>●大型テント／タープ／焚火台／テーブル／チェア×4</p>
      <div class="photo fire" role="img" aria-label="キャンプ場のタープとテントの写真"></div>
    </div>
  </section>

  <section class="others">
    <h2>その他個別レンタル品</h2>
    <table class="price-table">
      <tr><td>登山テント</td><td class="yen">¥2,500〜</td><td>天体望遠鏡</td><td class="yen">¥3,980〜</td></tr>
      <tr><td>寝袋</td><td class="yen">¥2,000〜</td><td>BBQセット</td><td class="yen">¥3,980〜</td></tr>
      <tr><td>大型ザック</td><td class="yen">¥1,500〜</td><td>釣りセット</td><td class="yen">¥2,980〜</td></tr>
    </table>
  </section>
  <div class="item-photos">
    <div class="photo grill" role="img" aria-label="バーベキューグリルの写真"></div>
    <div class="photo cooler" role="img" aria-label="クーラーボックスの写真"></div>
    <div class="photo scope" role="img" aria-label="天体望遠鏡の写真"></div>
  </div>
  <div class="more-badge">他にも様々な<br>レンタル品<br>あります</div>

  <p class="note">※価格は税込です。レンタル期間の延長や配送、返却方法についてはお気軽にお問い合わせください。<br>レンタル用品はすべて清掃・点検済みです。ご予約は電話またはホームページから承っております。</p>

  <footer class="store">
    <div class="store-label">店舗情報</div>
    <div class="store-name"><i class="mark"></i><span><small>アウトドアギアレンタル</small>こかげどう</span></div>
    <div class="contact">
      <p><span class="tag">WEB</span><span class="web">http://www.kokagedou.jp/</span></p>
      <p><span class="tag">所在地</span>〒418-0021 静岡県こもれび市緑ヶ丘1128-3</p>
      <p>営業時間：9:00〜19:00（7月〜8月は8:00〜20:00）</p>
      <p class="tel">TEL 0544-61-3917　FAX 0544-61-3918</p>
    </div>
    <div class="map" role="img" aria-label="店舗周辺の地図"></div>
    <div class="bottom-band"></div>
  </footer>

</main>
</body>
</html>
```